Create modern and sleek business card for luxury real estate company

We're a "boutique" real estate office looking for a design that gets across a highly modern luxury brand. Blacks and whites are probably the best colors unless we try a silver foil for the logo. I've attached a version of our current logo here. I'd like to swap out the current font on there with Gotham Light Regular.

I'm looking to have one side of the card have the logo with the space for our agents info on the other side.

Target Market(s)

Young professionals in a "luxury" headspace

Industry/Entity Type

Real estate

Contact Information for Business Card

A place for agent name, cell number, website. The slogan "Simply Rethinking Real Estate".

Font styles to use
Other font styles liked:
• Gotham Regular

Colors

Designer to choose only greyscale colors for use in the design.

Requirements
Must have
• Matte black as the background color. Clean lines and use of contrast. A specific design aspect that will use silver foil.
Nice to have
• Up in the air on integrating a QR code
Should not have
• Any houses or other real estate related design (ex: a clip art house)

```html
<!DOCTYPE html>
<html lang="en">
<head>
<meta charset="utf-8">
<title>Lumen Realty – Business Card</title>
<link href="https://fonts.googleapis.com/css2?family=Montserrat:wght@300;400;700&display=swap" rel="stylesheet">
<style>
  :root {
    --page-bg: #ffffff;
    --card-bg: #1c1f22;
    --ink: #ffffff;
    --band: #8e8e8e;
    --glow: rgba(120, 135, 135, 0.55);
  }
  html, body {
    margin: 0;
    padding: 0;
    width: 1200px;
    height: 1000px;
    overflow: hidden;
    background: var(--page-bg);
  }
  .canvas {
    position: relative;
    width: 1200px;
    height: 1000px;
    font-family: "Montserrat", sans-serif;
    color: var(--ink);
  }
  .card {
    position: absolute;
    left: 161px;
    top: 249px;
    width: 877px;
    height: 500px;
    background: var(--card-bg);
    box-shadow: 0 0 28px 10px var(--glow);
    overflow: hidden;
  }
  .agent-name {
    position: absolute;
    left: 61px;
    top: 60px;
    margin: 0;
    font-size: 37px;
    line-height: 1;
    letter-spacing: 0.5px;
    white-space: nowrap;
  }
  .agent-name .first { font-weight: 700; }
  .agent-name .last { font-weight: 300; }
  .tagline {
    position: absolute;
    left: 88px;
    top: 106px;
    margin: 0;
    font-size: 14.5px;
    font-weight: 400;
    letter-spacing: 0.2px;
    white-space: nowrap;
  }
  .rule {
    position: absolute;
    left: 80px;
    top: 143px;
  }
  .brand-name {
    position: absolute;
    right: 58px;
    top: 88px;
    margin: 0;
    font-size: 30px;
    font-weight: 300;
    line-height: 1;
    letter-spacing: 2px;
    white-space: nowrap;
  }
  .contact-list {
    position: absolute;
    left: 62px;
    top: 280px;
    margin: 0;
    padding: 0;
    list-style: none;
  }
  .contact-list li {
    display: flex;
    align-items: center;
    height: 24px;
    margin-bottom: 15px;
    font-size: 23px;
    font-weight: 300;
    letter-spacing: 2px;
    white-space: nowrap;
  }
  .contact-list svg {
    width: 26px;
    height: 24px;
    margin-right: 17px;
    fill: var(--ink);
  }
  .band {
    position: absolute;
    left: 0;
    top: 473px;
    width: 100%;
    height: 11px;
    background: var(--band);
  }
</style>
</head>
<body>
<div class="canvas">
  <section class="card">
    <h1 class="agent-name"><span class="first">DANIEL</span> <span class="last">REYES</span></h1>
    <p class="tagline">SIMPLY RETHINKING REAL ESTATE</p>
    <svg class="rule" width="271" height="6" viewBox="0 0 271 6" aria-hidden="true">
      <rect x="0" y="0" width="48" height="5" fill="#ffffff"/>
      <rect x="48" y="1.5" width="223" height="2" fill="#ffffff"/>
    </svg>

    <p class="brand-name">LUMEN REALTY</p>

    <ul class="contact-list">
      <li>
        <svg viewBox="0 0 26 24" aria-hidden="true"><path d="M13 1a7 7 0 0 0-7 7c0 5 7 14 7 14s7-9 7-14a7 7 0 0 0-7-7zm0 10a3 3 0 1 1 0-6 3 3 0 0 1 0 6z"/></svg>
        XXXXXXXXXXXXXXXXXX
      </li>
      <li>
        <svg viewBox="0 0 26 24" aria-hidden="true"><path d="M8 2l3 5-2 2c1 3 3 5 6 6l2-2 5 3-2 4c-8 0-14-7-14-14z"/></svg>
        XXXXXXXXXXXXXXXX
      </li>
      <li>
        <svg viewBox="0 0 26 24" aria-hidden="true"><path d="M2 5h22v14H2z" fill="none" stroke="#fff" stroke-width="2"/><path d="M2 5l11 9 11-9M2 19l8-7M24 19l-8-7" fill="none" stroke="#fff" stroke-width="2"/></svg>
        XXXXXXXXXXXXXXXX
      </li>
      <li>
        <svg viewBox="0 0 26 24" aria-hidden="true"><path d="M8 1v19l4-4 3 7 3-1-3-7h6z"/></svg>
        XXXXXXXXXXXXXXXX
      </li>
    </ul>

    <div class="band"></div>
  </section>
</div>
</body>
</html>
```